Lumen Audio and Ear Care Solutions - Let's help people glow with clearer sound!

I am a private practice audiologist that focuses on hearing and tinnitus treatment. My job allows me the opportunity to help people to improve their lives with better communication, connecting them with family, friends, the people that matter the most. I love what I do. The design should communicate warmth and professionalism. A modern approach to an affliction that effects people of all ages. A like a natural color pallet with turquoise as an accent. I just want something powerful that will motivate people to make an appointment.

Industry/Entity Type

Communication

```html
<!DOCTYPE html>
<html lang="en">
<head>
<meta charset="utf-8">
<title>Lumen Audio and Ear Care Solutions – Page Cover</title>
<link rel="stylesheet" href="https://fonts.googleapis.com/css2?family=PT+Sans:wght@400;700&family=Roboto:wght@400;700&display=swap">
<style>
  :root {
    --bar-blue: #3b5998;
    --bar-edge: #29487d;
    --page-bg: #e9ebf0;
    --card-white: #ffffff;
    --card-edge: #d3d6db;
    --teal: #3dd8c6;
    --teal-deep: #2ccbb8;
    --cover-window: #f6f4ef;
    --cover-cream: #ece4d8;
    --cover-warm: #d9c3a8;
    --cover-skin: #e2b89a;
    --cover-navy: #2c3448;
    --text-white: #ffffff;
    --button-text: #4b4f56;
    --button-edge: #ced0d4;
    --button-bg: #f6f7f9;
    --like-blue: #4267b2;
  }
  * { box-sizing: border-box; margin: 0; padding: 0; }
  html, body { width: 1200px; height: 481px; overflow: hidden; }
  body {
    position: relative;
    background: var(--page-bg);
    font-family: "PT Sans", Arial, sans-serif;
  }
  .top-bar {
    position: absolute; left: 0; top: 0;
    width: 1200px; height: 30px;
    background: var(--bar-blue);
    border-bottom: 1px solid var(--bar-edge);
  }
  .network-name {
    position: absolute; left: 217px; top: 4px;
    color: var(--text-white);
    font-family: "Roboto", Arial, sans-serif;
    font-size: 18px; font-weight: 700; letter-spacing: -0.4px;
  }
  .page-card {
    position: absolute; left: 216px; top: 30px;
    width: 729px; height: 421px;
    background: var(--card-white);
    border: 1px solid var(--card-edge);
    border-top: none;
  }
  .cover-photo {
    position: absolute; left: 0; top: 0;
    width: 727px; height: 270px;
    background:
      linear-gradient(180deg, rgba(40,30,25,0) 60%, rgba(40,30,25,0.35) 100%),
      radial-gradient(ellipse 120px 150px at 560px 230px, rgba(44,52,72,0.75), rgba(44,52,72,0) 100%),
      radial-gradient(ellipse 90px 110px at 680px 130px, rgba(217,180,140,0.8), rgba(217,180,140,0) 100%),
      radial-gradient(ellipse 90px 90px at 340px 110px, rgba(226,184,154,0.55), rgba(226,184,154,0) 100%),
      radial-gradient(ellipse 110px 130px at 160px 190px, rgba(60,58,62,0.35), rgba(60,58,62,0) 100%),
      linear-gradient(90deg, var(--cover-cream) 0%, var(--cover-window) 35%, var(--cover-window) 60%, var(--cover-cream) 85%, var(--cover-warm) 100%);
  }
  .profile-frame {
    position: absolute; left: 12px; top: 150px;
    width: 147px; height: 146px;
    background: var(--card-white);
    border: 1px solid var(--button-edge);
    padding: 4px;
  }
  .profile-logo {
    width: 100%; height: 100%;
    background: linear-gradient(160deg, var(--teal) 0%, var(--teal-deep) 100%);
    display: flex; flex-direction: column; align-items: center; justify-content: center;
    padding: 0 6px;
  }
  .profile-rule { width: 100%; height: 1px; background: var(--text-white); }
  .profile-name {
    color: var(--text-white);
    font-size: 12px; font-weight: 400; line-height: 1.25;
    text-align: center; text-transform: uppercase;
    padding: 4px 0;
  }
  .page-title {
    position: absolute; left: 169px; top: 213px;
    color: var(--text-white);
    text-shadow: 0 1px 3px rgba(0,0,0,0.55);
  }
  .page-title h1 { font-size: 21px; font-weight: 700; line-height: 26px; letter-spacing: 0.3px; }
  .page-title p { font-size: 15px; font-weight: 400; line-height: 18px; margin-top: 4px; }
  .actions { position: absolute; top: 236px; height: 23px; display: flex; }
  .actions.liked { left: 447px; }
  .actions.group { left: 530px; }
  .action-button {
    height: 23px;
    display: flex; align-items: center; justify-content: center; gap: 4px;
    background: var(--button-bg);
    border: 1px solid var(--button-edge);
    color: var(--button-text);
    font-family: "Roboto", Arial, sans-serif;
    font-size: 11px; font-weight: 700;
  }
  .action-button + .action-button { border-left: none; }
  .action-button.like { width: 72px; }
  .action-button.follow { width: 79px; }
  .action-button.message { width: 74px; }
  .action-button.more { width: 35px; }
  .action-button svg { display: block; }
</style>
</head>
<body>
  <header class="top-bar">
    <span class="network-name">Friendlink</span>
  </header>

  <main class="page-card">
    <div class="cover-photo" role="img" aria-label="Cover photo: a smiling audiologist in a white coat chatting warmly with an older man and a young woman, colleagues behind them in a bright office"></div>

    <div class="profile-frame">
      <div class="profile-logo">
        <div class="profile-rule"></div>
        <span class="profile-name">Lumen Audio and<br>Ear Care Solutions</span>
        <div class="profile-rule"></div>
      </div>
    </div>

    <div class="page-title">
      <h1>Lumen</h1>
      <p>Audio &amp; Ear Care Solutions</p>
    </div>

    <div class="actions liked">
      <div class="action-button like">
        <svg width="11" height="11" viewBox="0 0 11 11" aria-hidden="true">
          <rect x="0" y="4.5" width="2.5" height="6.5" fill="var(--like-blue)"/>
          <path d="M3.5 4.5 L6 0.5 Q7.5 0.5 7 3 L7 4 L10 4 Q11 4 10.8 5.2 L10 10 Q9.8 11 8.8 11 L3.5 11 Z" fill="var(--like-blue)"/>
        </svg>
        Liked
        <svg width="8" height="5" viewBox="0 0 8 5" aria-hidden="true"><path d="M0 0 L8 0 L4 5 Z" fill="var(--button-text)"/></svg>
      </div>
    </div>

    <div class="actions group">
      <div class="action-button follow">
        <svg width="10" height="8" viewBox="0 0 10 8" aria-hidden="true"><path d="M1 4 L4 7 L9 1" fill="none" stroke="var(--button-text)" stroke-width="1.8"/></svg>
        Following
      </div>
      <div class="action-button message">
        <svg width="10" height="10" viewBox="0 0 10 10" aria-hidden="true"><path d="M0 0 H10 V7 H4 L1.5 9.5 V7 H0 Z" fill="var(--button-text)"/></svg>
        Message
      </div>
      <div class="action-button more">
        <svg width="16" height="4" viewBox="0 0 16 4" aria-hidden="true">
          <circle cx="2" cy="2" r="2" fill="var(--button-text)"/>
          <circle cx="8" cy="2" r="2" fill="var(--button-text)"/>
          <circle cx="14" cy="2" r="2" fill="var(--button-text)"/>
        </svg>
      </div>
    </div>
  </main>
</body>
</html>
```